Chocoloate confectionery company requires vibrant Packaging Design for a mini chocolate bar

- Need a packaging design for a new product; a chocolate mini-bar.
- Our corporate colors of brown and pink should be included in design.
- The chocolate weighs 20grams and measures 8 cm length x 5 cm width x 1 cm depth
- It will be covered in gold foil and wrapped in a paper sleeve.
- The paper sleeve measures 13.5 cm length x 7.5 cm width
- The paper sleeve can then be sectioned into 3 equal areas
- The packaging design is required on middle section of the sleeve.
- The ingredients, company details, barcode and disclaimer etc will be on the right section
- The left section of the sleeve may be left blank

PLEASE SEE SAMPLE PICTURES PER ATTACHED

Target Market(s)

Everyday shoppers (e.g. Moms, Dads, kids, teens, students)

Industry/Entity Type

It Company

Requirements
Must have
• Brown and pink colors (as per business card attached)
Name of mini chocolate bar is Mello Drop. This must appear on middle section of paper sleeve

```html
<!DOCTYPE html>
<html lang="en">
<head>
<meta charset="utf-8">
<title>Mello Drop – Mini Bar Sleeve</title>
<link rel="stylesheet" href="https://fonts.googleapis.com/css2?family=Dancing+Script:wght@500;700&display=swap">
<style>
  :root {
    --page: #ffffff;
    --band-top: #7a2b2b;
    --band-bottom: #6b2828;
    --sleeve: #f09a84;
    --fold: #f6b9a8;
    --brand: #7c2a2f;
    --accent: #d8326a;
    --info: #d8326a;
    --choc-dark: #6e2f22;
    --choc-light: #9a5430;
  }
  html, body {
    margin: 0;
    width: 1200px;
    height: 711px;
    overflow: hidden;
    background: var(--page);
  }
  .sleeve {
    display: block;
    width: 1200px;
    height: 711px;
    font-family: "Dancing Script", cursive;
  }
  .band-top { fill: var(--band-top); }
  .band-bottom { fill: var(--band-bottom); }
  .sleeve-body { fill: var(--sleeve); }
  .fold-line { stroke: var(--fold); stroke-width: 1; }
  .product-name { fill: var(--brand); font-size: 68px; font-weight: 700; }
  .name-rule { fill: var(--accent); }
  .info-text { fill: var(--info); font-size: 23px; font-weight: 500; }
  .info-heading { font-size: 31px; font-weight: 700; text-decoration: underline; }
  .origin { font-size: 23px; letter-spacing: 1px; }
</style>
</head>
<body>
<svg class="sleeve" viewBox="0 0 1200 711" xmlns="http://www.w3.org/2000/svg">
  <defs>
    <linearGradient id="choc-fill" x1="0" y1="0" x2="1" y2="1">
      <stop offset="0" stop-color="var(--choc-dark)"/>
      <stop offset="1" stop-color="var(--choc-light)"/>
    </linearGradient>
  </defs>

  <rect class="sleeve-body" x="61" y="43" width="1076" height="597"/>
  <path class="band-top" d="M61 43 H1137 V104 Q599 46 61 104 Z"/>
  <path class="band-bottom" d="M61 486 Q599 644 1137 486 V640 H61 Z"/>
  <line class="fold-line" x1="420" y1="76" x2="420" y2="560"/>
  <line class="fold-line" x1="778" y1="76" x2="778" y2="560"/>

  <g class="front-panel">
    <rect class="product-visual" role="img" aria-label="Illustration of a bitten chocolate bar"
      x="472" y="100" width="262" height="220" rx="10" fill="url(#choc-fill)"/>
    <text class="product-name" x="590" y="448" text-anchor="middle">Mello Drop</text>
    <rect class="name-rule" x="513" y="483" width="247" height="10"/>
    <rect class="name-rule" x="540" y="503" width="220" height="10"/>
  </g>

  <g class="info-panel info-text" text-anchor="middle">
    <text x="956" y="131"><tspan class="info-heading">Ingredients:</tspan> Sugar,</text>
    <text x="956" y="167">Soya, Hydrogenerated</text>
    <text x="956" y="198">vegetable fat (Palm Kernel),</text>
    <text x="956" y="230">Maltedextrin low fat rocca</text>
    <text x="956" y="262">powder, whip powder</text>
    <text x="956" y="293">(milk),Leathin,Flavouring,</text>
    <text x="956" y="340"><tspan class="info-heading">Allergies:</tspan> Contains cow</text>
    <text x="956" y="376">milk, Soya bean, may</text>
    <text x="956" y="406">contain tree nuts.</text>
    <text class="origin" x="956" y="456">Handmade in Zimbabwe</text>
    <text class="origin" x="956" y="493">“Contact details”</text>
  </g>
</svg>
</body>
</html>
```